New Website for NY and South Florida Based Accounting Firm

Accounting and Audit firm located in New York and South Florida needs a website redesign after acquiring new businesses and adding new services.

Our current website can be found here:
http://www.tkrbwco.example/

We have merged with this firm:
http://halloranbeckwithstrand.example/

We are looking for a comprehensive design that will highlight the firm's dual locations. The final design should communicate security, strength, and growth. We would like to keep our pyramid logo as seen on the tkrbwco.example website, as this has been our logo for over 20 years.

Industry/Entity Type

Accounting

Number of Pages Required

1 page

Font styles to use
Serif
Sans Serif

```html
<!DOCTYPE html>
<html lang="en">
<head>
<meta charset="utf-8">
<title>Tarrant, Kessler, Rourke &amp; Bainbridge, LLP — Profiles</title>
<link href="https://fonts.googleapis.com/css2?family=Arimo:wght@400;700&family=Open+Sans:ital,wght@0,400;0,700;1,400&family=Libre+Baskerville:wght@700&display=swap" rel="stylesheet">
<style>
:root{
  --orange:#d88a2b;
  --orange-soft:#e3a04a;
  --navy:#1d2f48;
  --ink:#1a1f2b;
  --body:#6b6b6b;
  --rule:#dcdcdc;
  --white:#ffffff;
}
*{margin:0;padding:0;box-sizing:border-box}
html,body{width:1200px;height:2423px;overflow:hidden;background:var(--white)}
body{position:relative;font-family:"Open Sans",Arial,sans-serif;color:var(--body)}
.abs{position:absolute}

.site-header{left:0;top:0;width:1200px;height:95px;background:var(--white)}
.brand{left:100px;top:20px;display:flex;align-items:center;gap:14px}
.brand-mark{width:52px;height:52px;background:var(--orange)}
.brand-name{font-family:"Libre Baskerville",Georgia,serif;font-weight:700;font-size:14px;line-height:20px;color:var(--ink);width:200px}
.main-nav{right:96px;top:41px;display:flex;gap:21px;font-family:"Arimo",Arial,sans-serif;font-weight:700;font-size:12.5px;color:var(--ink)}
.main-nav .active{color:var(--orange);border-bottom:2px solid var(--orange);padding-bottom:4px}
.nav-search{width:14px;height:14px;margin-top:-1px}

.hero{left:0;top:95px;width:1200px;height:318px;background:linear-gradient(90deg,#8a7a62 0%,#4e5968 25%,#33475f 50%,#5a6c80 72%,#cfd6dc 100%)}
.hero-title{left:0;top:178px;width:1200px;text-align:center;font-family:"Arimo",Arial,sans-serif;font-weight:700;font-size:46px;color:var(--white);letter-spacing:1px}
.hero-dots{left:570px;top:276px;display:flex;gap:4px}
.hero-dots span{width:13px;height:13px;border-radius:50%;border:2px solid var(--white)}
.hero-dots span.on{background:var(--orange)}

.about-photo{left:98px;top:454px;width:419px;height:260px;border:4px solid #eee;background:linear-gradient(160deg,#e9ecef 0%,#c8ced4 45%,#3b3f48 75%,#8fa0a8 100%)}
.about-title{left:555px;top:452px;font-family:"Arimo",Arial,sans-serif;font-weight:700;font-size:19px;color:var(--ink)}
.about-text{left:555px;top:492px;width:550px;font-size:12.5px;line-height:26.5px}
.about-text p+p{margin-top:26px}
.read-more{left:553px;top:697px;font-weight:700;font-size:12.5px;color:var(--orange)}
.divider{left:100px;top:753px;width:1005px;height:1px;background:var(--rule)}

.team-title{left:0;top:785px;width:1200px;text-align:center;font-family:"Arimo",Arial,sans-serif;font-weight:700;font-size:20px;color:var(--ink)}
.member{width:300px}
.member-photo{width:140px;height:140px;border-radius:50%;border:4px solid #e4e4e4;background:radial-gradient(circle at 50% 40%,#d9cbbd 0%,#b9a998 30%,#3a3f4a 70%,#f0f0f0 71%)}
.member-name{margin-top:24px;font-family:"Arimo",Arial,sans-serif;font-weight:700;font-size:14.5px;color:var(--ink);letter-spacing:.3px}
.member-role{margin-top:6px;font-family:"Arimo",Arial,sans-serif;font-style:italic;font-size:14.5px;color:var(--orange)}
.member-bio{margin-top:11px;font-size:12.3px;line-height:24.2px}

.site-footer{left:0;top:2007px;width:1200px;height:416px;background:linear-gradient(180deg,#bcc3c9 0%,#8e979f 45%,#565d68 100%)}
.footer-art{left:0;top:1920px}
.footer-contact{left:300px;top:2120px;width:600px;text-align:center;font-family:"Arimo",Arial,sans-serif;color:var(--white);font-size:15px;line-height:32px}
.footer-contact svg{vertical-align:-2px;margin-right:8px}
.office{width:400px;text-align:center;font-family:"Arimo",Arial,sans-serif;color:var(--white)}
.office h3{font-size:14.5px;font-weight:700;margin-bottom:14px}
.office p{font-size:12.5px;line-height:22px}
.social{left:524px;top:2227px;display:flex;gap:12px}
</style>
</head>
<body>

<header class="site-header abs">
  <div class="brand abs">
    <span class="brand-mark"></span>
    <span class="brand-name">Tarrant, Kessler, Rourke &amp; Bainbridge, LLP</span>
  </div>
  <nav class="main-nav abs">
    <span>HOME</span><span>WHY TKRB?</span><span>SERVICES</span><span class="active">PROFILES</span><span>TIPS &amp; LINKS</span><span>CLIENT LOGIN</span><span>CONTACT</span>
    <svg class="nav-search" viewBox="0 0 14 14"><circle cx="6" cy="6" r="4.3" fill="none" stroke="#1a1f2b" stroke-width="2"/><line x1="9" y1="9" x2="13" y2="13" stroke="#1a1f2b" stroke-width="2.2"/></svg>
  </nav>
</header>

<section class="hero abs" role="img" aria-label="Upward view of city office towers against the sky"></section>
<h1 class="hero-title abs">PROFILES</h1>
<div class="hero-dots abs"><span class="on"></span><span></span><span></span><span></span></div>

<div class="about-photo abs" role="img" aria-label="Team of accountants smiling around a laptop in the office"></div>
<h2 class="about-title abs">A FEW WORD ABOUT US</h2>
<div class="about-text abs">
  <p>Tarrant, Kessler, Rourke &amp; Bainbridge, LLP is an accounting, audit and business management firm with offices in New York City, Long Island, and Florida. Our experienced CPA's offer financial solutions and vast resources in all aspects of accounting, tax planning, tax return preparation, personal financial planning, estate and trust, and small business consulting.</p>
  <p>Our services are backed by a commitment to one-on-one attention and an unwavering dedication to meeting the highest business standards.</p>
</div>
<span class="read-more abs">READ MORE &gt;&gt;</span>
<div class="divider abs"></div>

<h2 class="team-title abs">TEAM MEMBERS</h2>

<article class="member abs" style="left:100px;top:840px">
  <div class="member-photo" role="img" aria-label="Portrait of Thomas C. Tarrant"></div>
  <h3 class="member-name">THOMAS C. TARRANT, CPA, P.C.</h3>
  <div class="member-role">Managing Partner</div>
  <p class="member-bio">Thomas C. Tarrant has been a certified public accountant for over twenty years. Mr. Tarrant has extensive experience in taxation, estate planning and personal financial planning. He is a member of the National Institute of Certified Public Accountants, the Empire State Society of Certified Public Accountants, and the NICPA Personal Financial Planning Division. Mr. Tarrant has also been the managing partner of the firm for the last 10 years and brings his years of management experience and expertise to his clients.</p>
</article>

<article class="member abs" style="left:453px;top:840px">
  <div class="member-photo" role="img" aria-label="Portrait of David J. Kessler"></div>
  <h3 class="member-name">DAVID J. KESSLER CPA, P.C.</h3>
  <div class="member-role">Senior Partner</div>
  <p class="member-bio">David J. Kessler graduated from Eastbrook University in 1980 with a Bachelor of Science degree in accounting. He is a member of the National Institute of Certified Public Accountants and the Empire State Society of Certified Public Accountants. Mr. Kessler has comprehensive experience in taxation, auditing, business valuations and personal financial planning. Mr. Kessler has also lectured extensively and is an expert on the subject of Personal Financial Planning.</p>
</article>

<article class="member abs" style="left:805px;top:840px">
  <div class="member-photo" role="img" aria-label="Portrait of Richard Rourke"></div>
  <h3 class="member-name">RICHARD ROURKE CPA, P.C.</h3>
  <div class="member-role">Partner</div>
  <p class="member-bio">Richard Rourke graduated Harborview College with a Bachelor of Business Administration in accounting. Mr. Rourke has a diverse clientele and specializes in the areas of estates and trusts; real estate developers and investors; and construction contractors. He is a member of the National Institute of Certified Public Accountants and the Empire State Society of Certified Public Accountants.</p>
</article>

<article class="member abs" style="left:100px;top:1350px">
  <div class="member-photo" role="img" aria-label="Portrait of Simon Bainbridge"></div>
  <h3 class="member-name">SIMON BAINBRIDGE, CPA</h3>
  <div class="member-role">Partner</div>
  <p class="member-bio">Simon Bainbridge graduated Summa Cum Laude from Northfield University with a Bachelors Degree in Accounting. He began his professional career at Ledgerline Partners, a global leader providing audit, tax and advisory services to some of the world's largest companies. He later served as Controller and Chief Financial Officer for big business, including a Top 500 company as well as a division of Ashcombe investments.<br>Today Simon focuses on offering part-time controller and CFO advisory services to small and medium size business clients. His objective is to understand their financial position and needs so that their business decisions are supported by intelligent, accurate and reliable financial data.</p>
</article>

<article class="member abs" style="left:453px;top:1350px">
  <div class="member-photo" role="img" aria-label="Portrait of Patricia S. Wren"></div>
  <h3 class="member-name">PATRICIA S. WREN CPA, P.C.</h3>
  <div class="member-role">Partner</div>
  <p class="member-bio">Patricia S. Wren has a Master of Science degree from The Meadow School of Accountancy at Hollis University and a Master of Arts degree from Northfield University's Graduate School of Arts and Sciences. She has been with the firm 15 years and has wide-ranging experience with our diversified client base. Mrs. Wren is a member of the National Institute of Certified Public Accountants, the Empire State Society of Certified Public Accountants and NAWE – the National Alliance of Women Executives.</p>
</article>

<article class="member abs" style="left:805px;top:1350px">
  <div class="member-photo" role="img" aria-label="Portrait of Brian A. Cole"></div>
  <h3 class="member-name">BRIAN A. COLE, CPA, P.C.</h3>
  <div class="member-role">Partner</div>
  <p class="member-bio">Brian A. Cole has been a certified public accountant since 1987. He graduated from Eastbrook University with a Bachelor of Science degree in accounting. Mr. Cole has comprehensive experience in individual, corporate, partnership and estate taxation. He oversees all tax matters for the firm. Mr. Cole lectures on various tax matters. He is a member of the National Institute of Certified Public Accountants and the Empire State Society of Certified Public Accountants.</p>
</article>

<footer class="site-footer abs" role="img" aria-label="City street with office buildings at dusk"></footer>
<svg class="footer-art abs" width="1200" height="503" viewBox="0 1920 1200 503">
  <polygon points="102,2358 700,2358 400,2140" fill="#1d2f48" opacity=".92"/>
  <polygon points="500,2358 1098,2358 800,2140" fill="#1d2f48" opacity=".92"/>
  <polygon points="600,1922 848,2136 600,2350 352,2136" fill="#d88a2b" opacity=".93"/>
</svg>

<div class="footer-contact abs">
  <div>
    <svg width="14" height="14" viewBox="0 0 14 14"><path d="M3 1l2.5 3-1.5 1.5c.8 1.8 2.2 3.2 4 4L9.5 8l3 2.5-1.5 2.5C6 12.5 1.5 8 1 3z" fill="#fff"/></svg>555-010-8989 &nbsp;| &nbsp;<svg width="14" height="14" viewBox="0 0 14 14"><rect x="2" y="1" width="10" height="12" fill="none" stroke="#fff" stroke-width="2"/><line x1="4.5" y1="5" x2="9.5" y2="5" stroke="#fff" stroke-width="1.5"/><line x1="4.5" y1="8.5" x2="9.5" y2="8.5" stroke="#fff" stroke-width="1.5"/></svg>555-010-8993
  </div>
  <div><svg width="16" height="12" viewBox="0 0 16 12"><rect width="16" height="12" fill="#fff"/><polyline points="0,0 8,6 16,0" fill="none" stroke="#d88a2b" stroke-width="1.5"/></svg>Send Us An Email</div>
  <div>© 2016 TKRB. All right Reserved.</div>
</div>

<svg class="social abs" width="152" height="44" viewBox="0 0 152 44">
  <polygon points="22,1 43,22 22,43 1,22" fill="none" stroke="#fff" stroke-width="1.5"/>
  <polygon points="76,1 97,22 76,43 55,22" fill="none" stroke="#fff" stroke-width="1.5"/>
  <polygon points="130,1 151,22 130,43 109,22" fill="none" stroke="#fff" stroke-width="1.5"/>
</svg>

<div class="office abs" style="left:200px;top:2238px">
  <h3>New York City Office</h3>
  <p>210 Harbor Avenue &nbsp;2nd Floor<br>New York, NY 10001</p>
</div>
<div class="office abs" style="left:600px;top:2238px">
  <h3>Florida Office</h3>
  <p>480 Palm Crest Blvd, Suite 201<br>Fort Lauderdale, FL 33309</p>
</div>

</body>
</html>
```